We have developed a fully functional App called Corvalink. However, it requires a nicer GUI. You can see screenshots of our App on www.corvalink-example.com under "Tutorial". For those of you with Android, you can also install it. When you go to Corvalink-example.com, your phone will automatically redirect you to download. From there, you'll get a better idea of what our App looks like and how your design can make it way better. Please note we expect a design idea for most screens (there's about 8 screens) but do just one screen first and if you win, you can do the other 8 after.

Target Market(s)

People looking for dating / flirting

Industry/Entity Type

Android

Requirements
Must have
• sleek looking

```html
<!DOCTYPE html>
<html lang="en">
<head>
<meta charset="utf-8">
<title>Corvalink – Message list</title>
<link rel="stylesheet" href="https://fonts.googleapis.com/css2?family=Roboto:wght@400;500;700&display=swap">
<style>
  :root {
    --page-bg: #efefef;
    --header-top: #f2f2f2;
    --header-bottom: #d9d9d9;
    --accent: #3eaee0;
    --accent-dark: #2e95c6;
    --tab-bg: #50c0ea;
    --tab-active: #3aa9da;
    --row-grey: #cbcbcb;
    --row-blue: #a7e2f9;
    --text-dark: #5a5a5a;
    --text-mid: #666666;
    --ring: #999999;
    --online: #19b21e;
    --away: #e0a300;
    --offline: #a9a9a9;
    --chevron: #9a9a9a;
    --white: #ffffff;
  }
  * { box-sizing: border-box; margin: 0; padding: 0; }
  html, body {
    width: 713px; height: 1200px; overflow: hidden;
    background: var(--page-bg);
    font-family: "Roboto", Arial, sans-serif;
  }
  .app-screen {
    position: absolute; left: 103px; top: 220px;
    width: 500px; height: 748px;
    background: var(--white);
    overflow: hidden;
  }
  .top-bar {
    position: absolute; left: 0; top: 0; width: 500px; height: 70px;
    background: linear-gradient(var(--header-top), var(--header-bottom));
    border-bottom: 2px solid #c8c8c8;
  }
  .icon-button {
    position: absolute; top: 16px; width: 56px; height: 38px;
    background: var(--accent); border-radius: 3px;
    box-shadow: 0 2px 0 var(--accent-dark);
    display: flex; align-items: center; justify-content: center;
  }
  .icon-button.back { left: 14px; }
  .icon-button.refresh { left: 428px; }
  .brand {
    position: absolute; left: 0; right: 0; top: 0; height: 70px;
    display: flex; align-items: center; justify-content: center; gap: 10px;
  }
  .brand-dot { width: 30px; height: 30px; border-radius: 50%; background: var(--accent); }
  .brand-name { font-size: 32px; font-weight: 500; color: #4d4d4d; letter-spacing: 0.5px; }
  .contact-list {
    position: absolute; left: 6px; top: 77px; width: 487px;
    list-style: none;
  }
  .contact {
    position: relative; height: 124px; margin-bottom: 5px;
    background: var(--row-grey); border-radius: 2px;
  }
  .contact:nth-child(2) { margin-bottom: 5px; }
  .contact.highlight { background: var(--row-blue); }
  .avatar {
    position: absolute; left: 10px; top: 7px; width: 110px; height: 110px;
    border-radius: 50%; border: 5px solid var(--ring);
  }
  .avatar.tone-violet { background: radial-gradient(circle at 45% 40%, #b88f8a, #4a3550 60%, #2c2236); }
  .avatar.tone-night { background: radial-gradient(circle at 50% 45%, #b06a7a, #4b3a5a 60%, #1f1d35); }
  .avatar.tone-sun { background: radial-gradient(circle at 45% 45%, #f0d4b0, #d7a86a 55%, #9b7a4f); }
  .avatar.tone-brick { background: radial-gradient(circle at 50% 50%, #c79b7e, #6b4a3a 60%, #3a2a22); }
  .name { position: absolute; left: 143px; top: 13px; font-size: 16px; font-weight: 700; color: var(--text-dark); }
  .tagline { position: absolute; left: 143px; top: 38px; font-size: 12px; color: var(--text-mid); }
  .city { position: absolute; left: 146px; top: 88px; font-size: 14px; font-weight: 500; color: var(--text-dark); }
  .country { position: absolute; left: 147px; top: 106px; font-size: 11px; font-weight: 500; color: var(--text-dark); }
  .status { position: absolute; left: 397px; top: 100px; display: flex; align-items: center; gap: 9px; font-size: 14px; color: var(--text-mid); }
  .status-dot { width: 18px; height: 18px; border-radius: 50%; }
  .status.online .status-dot { background: var(--online); }
  .status.away .status-dot { background: var(--away); }
  .status.offline .status-dot { background: var(--offline); }
  .new-mail { position: absolute; left: 362px; top: 103px; }
  .chevron { position: absolute; left: 465px; top: 36px; }
  .tab-bar {
    position: absolute; left: 0; top: 663px; width: 500px; height: 85px;
    display: flex; background: var(--tab-bg);
  }
  .tab {
    display: flex; flex-direction: column; align-items: center; justify-content: center; gap: 8px;
    color: var(--white); font-size: 16px; font-weight: 500;
    border-right: 1px solid #6fcdee;
  }
  .tab.main { width: 174px; }
  .tab.message { width: 177px; background: var(--tab-active); }
  .tab.settings { width: 149px; border-right: none; }
</style>
</head>
<body>
<main class="app-screen">
  <header class="top-bar">
    <div class="icon-button back" aria-label="Back">
      <svg width="20" height="24" viewBox="0 0 20 24"><path d="M14 3 L5 12 L14 21" fill="none" stroke="#fff" stroke-width="4" stroke-linecap="round" stroke-linejoin="round"/></svg>
    </div>
    <div class="brand">
      <span class="brand-dot"></span>
      <span class="brand-name">Corvalink</span>
    </div>
    <div class="icon-button refresh" aria-label="Refresh">
      <svg width="30" height="26" viewBox="0 0 30 26">
        <path d="M5 12 A10 10 0 0 1 23 7" fill="none" stroke="#fff" stroke-width="3.5" stroke-linecap="round"/>
        <path d="M25 2 L25 10 L17 10 Z" fill="#fff"/>
        <path d="M25 14 A10 10 0 0 1 7 19" fill="none" stroke="#fff" stroke-width="3.5" stroke-linecap="round"/>
        <path d="M5 24 L5 16 L13 16 Z" fill="#fff"/>
      </svg>
    </div>
  </header>

  <ul class="contact-list">
    <li class="contact">
      <div class="avatar tone-violet" role="img" aria-label="Profile photo of Sweetguy"></div>
      <p class="name">Sweetguy, 29</p>
      <p class="tagline">"! Sweet, Never sour"</p>
      <p class="city">New York</p>
      <p class="country">U.S.A</p>
      <p class="status online"><span class="status-dot"></span>Online</p>
      <svg class="chevron" width="18" height="28" viewBox="0 0 18 28"><path d="M3 2 L15 14 L3 26" fill="none" stroke="var(--chevron)" stroke-width="2.5"/></svg>
    </li>
    <li class="contact highlight">
      <div class="avatar tone-night" role="img" aria-label="Profile photo of Sensual Mirela"></div>
      <p class="name">Sensual Mirela, 25</p>
      <p class="tagline">!!!Goodess and Temptress lives here</p>
      <p class="city">New York</p>
      <p class="country">U.S.A</p>
      <p class="status online"><span class="status-dot"></span>Online</p>
      <svg class="chevron" width="18" height="28" viewBox="0 0 18 28"><path d="M3 2 L15 14 L3 26" fill="none" stroke="var(--chevron)" stroke-width="2.5"/></svg>
    </li>
    <li class="contact">
      <div class="avatar tone-sun" role="img" aria-label="Profile photo of Sweetguy"></div>
      <p class="name">Sweetguy, 29</p>
      <p class="tagline">"! Sweet, Never sour"</p>
      <p class="city">New York</p>
      <p class="country">U.S.A</p>
      <svg class="new-mail" width="20" height="14" viewBox="0 0 20 14" aria-label="New message"><rect x="0.5" y="0.5" width="19" height="13" fill="#888" stroke="#777"/><path d="M1 1 L10 8 L19 1" fill="none" stroke="#ddd" stroke-width="1.2"/></svg>
      <p class="status away"><span class="status-dot"></span>Away</p>
      <svg class="chevron" width="18" height="28" viewBox="0 0 18 28"><path d="M3 2 L15 14 L3 26" fill="none" stroke="var(--chevron)" stroke-width="2.5"/></svg>
    </li>
    <li class="contact highlight">
      <div class="avatar tone-brick" role="img" aria-label="Profile photo of Marco Velani"></div>
      <p class="name">Marco Velani, 30</p>
      <p class="tagline">"! Sweet, Never sour"</p>
      <p class="city">New York</p>
      <p class="country">U.S.A</p>
      <p class="status offline"><span class="status-dot"></span>Offline</p>
      <svg class="chevron" width="18" height="28" viewBox="0 0 18 28"><path d="M3 2 L15 14 L3 26" fill="none" stroke="var(--chevron)" stroke-width="2.5"/></svg>
    </li>
    <li class="contact">
      <div class="avatar tone-violet" role="img" aria-label="Profile photo of Sweetguy"></div>
      <p class="name">Sweetguy, 29</p>
      <p class="tagline">"! Sweet, Never sour"</p>
      <svg class="chevron" width="18" height="28" viewBox="0 0 18 28"><path d="M3 2 L15 14 L3 26" fill="none" stroke="var(--chevron)" stroke-width="2.5"/></svg>
    </li>
  </ul>

  <nav class="tab-bar">
    <div class="tab main">
      <svg width="34" height="18" viewBox="0 0 34 18"><rect y="0" width="34" height="3" fill="#fff"/><rect y="7.5" width="34" height="3" fill="#fff"/><rect y="15" width="34" height="3" fill="#fff"/></svg>
      <span>Main</span>
    </div>
    <div class="tab message">
      <svg width="26" height="18" viewBox="0 0 26 18"><rect x="1" y="1" width="24" height="16" fill="none" stroke="#fff" stroke-width="2"/><path d="M1 1 L13 11 L25 1" fill="none" stroke="#fff" stroke-width="2"/></svg>
      <span>Message</span>
    </div>
    <div class="tab settings">
      <svg width="26" height="26" viewBox="0 0 26 26"><circle cx="13" cy="13" r="9" fill="none" stroke="#fff" stroke-width="4" stroke-dasharray="3.5 3.57"/><circle cx="13" cy="13" r="7" fill="none" stroke="#fff" stroke-width="2"/><circle cx="13" cy="13" r="3" fill="none" stroke="#fff" stroke-width="2"/></svg>
      <span>Settings</span>
    </div>
  </nav>
</main>
</body>
</html>
```